Web Design for a Biotech Consulting Firm

We need a web site design for a new business based in Philadelphia called Corventa Dx. This is a consulting firm that will serve medical diagnostics industry, which is part of the life science/healthcare industry focusing on developing and marketing products that help in early detection, monitoring or management of diseases. Our consulting firm will help medical diagnostic companies to overcome key challenges in designing, evaluating and marketing new products.Our company name is Corventa Dx. Corventa is Latin word for "something" Dx represents diagnostics. The idea behind the name is that we help companies to transform the original, early product ideas ("nothing") into "something"; which is a product with full clinical utility that will help to improve health and well-being.The web site should use the visual feel of the logo (attached), be modern, simple and clean looking and represent creativity, innovation, scientific thinking and progress.
Updates

Wix Design is acceptable

Industry/Entity Type

Biotechnology

Coding

Coded - Design and coding required

Number of Pages Required

1 page

Font styles to use
Sans Serif

Requirements
Must have
• simple, clean look couple of pages
Should not have
• a lot of pages

```html
<!DOCTYPE html>
<html lang="en">
<head>
<meta charset="utf-8">
<title>Corventa Dx</title>
<link href="https://fonts.googleapis.com/css2?family=Montserrat:wght@300;400;500;600;700&display=swap" rel="stylesheet">
<style>
:root{
  --blue:#1a7ff0;
  --blue-deep:#0f5fd0;
  --ink:#111316;
  --text:#3c3f44;
  --dark:#3a3a3d;
  --dark-2:#2e2f33;
  --white:#ffffff;
  --foot:#ececec;
  --rule:#cfd3d8;
}
*{margin:0;padding:0;box-sizing:border-box}
html,body{width:1200px;height:4500px;overflow:hidden;background:var(--white)}
body{position:relative;font-family:"Montserrat",sans-serif;color:var(--text)}
.abs{position:absolute}
.btn{position:absolute;display:flex;align-items:center;justify-content:center;border-radius:20px;font-size:12px;font-weight:500;color:var(--white);background:var(--blue);height:38px}
.btn--ghost{background:transparent;border:1.5px solid var(--white);height:30px;font-size:10px}
.photo{position:absolute}
.para{position:absolute;font-size:12px;line-height:26px;font-weight:400;color:var(--text)}
.blue{color:var(--blue)}

/* hero */
.hero{position:absolute;left:0;top:0;width:1200px;height:590px;background:linear-gradient(100deg,#3f8fb0 0%,#5ba9c7 35%,#8cc4d8 60%,#b7d6e2 100%);overflow:hidden}
.hero__veil{position:absolute;inset:0;background:linear-gradient(90deg,rgba(30,110,150,.55),rgba(30,110,150,0) 60%)}
.logo{position:absolute;left:163px;top:26px;width:70px;height:70px;border:2px solid var(--white);border-right-color:transparent;display:flex;align-items:center;padding-left:10px;color:var(--white);font-size:14px;font-weight:500;white-space:nowrap}
.nav{position:absolute;top:52px;left:405px;font-size:11px;color:var(--white)}
.nav span{position:absolute;white-space:nowrap}
.hero__title{position:absolute;left:150px;top:178px;font-size:58px;font-weight:600;color:var(--white);letter-spacing:-1px;white-space:nowrap}
.hero__text{position:absolute;left:152px;top:272px;width:380px;font-size:11.5px;line-height:25px;color:var(--white)}
.phone{position:absolute;left:888px;top:54px;font-size:11px;color:var(--white);white-space:nowrap}
.arrow{position:absolute;top:286px}

/* about */
.section-title{position:absolute;width:1200px;left:0;text-align:center;font-size:38px;font-weight:600;color:var(--ink)}
.rule{position:absolute;height:2px;background:var(--ink)}
.wedge{position:absolute}

/* services */
.services{position:absolute;left:0;top:1004px;width:1200px;height:804px;background:radial-gradient(ellipse at 25% 30%,#4a4b50 0%,var(--dark) 45%,var(--dark-2) 100%)}
.box-title{position:absolute;border:2px solid}
.card{position:absolute;top:1286px;width:288px}
.card__img{width:288px;height:201px;position:relative}
.card__icon{position:absolute;left:0;top:0;width:73px;height:66px;background:var(--blue);display:flex;align-items:center;justify-content:center}
.card__title{margin:30px 0 0 20px;font-size:23px;font-weight:500;color:var(--white)}
.card__text{margin:14px 0 0 20px;font-size:11.5px;line-height:26px;color:#e6e6e6;width:250px}
.card__link{margin:14px 0 0 20px;font-size:11px;color:var(--white);text-decoration:underline}
.dot-btn{position:absolute;width:34px;height:34px;border-radius:50%;background:var(--white);display:flex;align-items:center;justify-content:center}

/* features */
.frame{position:absolute;border:7px solid var(--ink)}
.feature__title{position:absolute;font-size:30px;font-weight:500;color:var(--ink);line-height:39px;white-space:nowrap}

/* testimonial */
.testimonial{position:absolute;left:0;top:3144px;width:1200px;height:542px;background:linear-gradient(120deg,#0f6fe0 0%,#2a8ff2 50%,#1876e6 100%);clip-path:polygon(0 105px,1200px 0,1200px 437px,0 542px)}
.avatar{position:absolute;left:546px;top:3261px;width:106px;height:106px;border-radius:50%;background:linear-gradient(#e7e9ec,#c9ced4);border:3px solid var(--white)}
.dots{position:absolute;left:578px;top:3569px;display:flex;gap:6px}
.dots i{width:8px;height:8px;border-radius:50%;background:rgba(255,255,255,.55)}
.dots i.on{background:var(--white)}

/* blog */
.meta{position:absolute;display:flex;align-items:center;gap:6px;font-size:10px;font-weight:600;color:var(--blue);white-space:nowrap}
.post-title{position:absolute;font-size:23px;font-weight:500;color:var(--ink);white-space:nowrap}
.more{position:absolute;font-size:11px;color:var(--blue);text-decoration:underline}
.divider{position:absolute;left:545px;width:433px;height:1px;background:var(--rule)}

/* footer */
.footer{position:absolute;left:0;top:4394px;width:1200px;height:106px;background:var(--foot)}
.footer__links span{position:absolute;top:34px;font-size:11px;font-weight:600;color:var(--ink);white-space:nowrap}
.footer__copy{position:absolute;left:206px;top:66px;font-size:11px;color:var(--text);white-space:nowrap}
.social{position:absolute;top:38px;width:30px;height:30px;background:var(--blue-deep)}
</style>
</head>
<body>

<!-- HERO -->
<header class="hero">
  <div class="photo" style="left:560px;top:0;width:640px;height:590px;background:radial-gradient(ellipse at 60% 45%,#d9e8ee 0%,#9fc6d6 45%,rgba(95,168,199,0) 80%)" role="img" aria-label="Scientist in goggles and gloves pipetting into test tubes"></div>
  <div class="hero__veil"></div>
  <div class="logo">Corventa Dx</div>
  <nav class="nav">
    <span style="left:0">Home</span>
    <span style="left:70px">About Us</span>
    <span style="left:158px">Services</span>
    <span style="left:238px">Blog</span>
    <span style="left:299px">Contact Us</span>
  </nav>
  <svg class="abs" style="left:802px;top:48px" width="24" height="24" viewBox="0 0 24 24"><circle cx="10" cy="10" r="7" fill="none" stroke="#fff" stroke-width="2.5"/><line x1="15" y1="15" x2="22" y2="22" stroke="#fff" stroke-width="3"/></svg>
  <svg class="abs" style="left:850px;top:50px" width="20" height="20" viewBox="0 0 24 24"><path d="M6 2l4 4-2 3c1 3 4 6 7 7l3-2 4 4-3 4C10 22 2 14 2 5z" fill="#fff"/></svg>
  <span class="phone">+215-555-0190</span>
  <h1 class="hero__title">Corventa Dx</h1>
  <p class="hero__text">Lorem Ipsum is simply dummy text of the printing and typesetting industry. Lorem Ipsum has been the industry's standard dummy text ever since the 1500s.</p>
  <span class="btn btn--ghost" style="left:150px;top:362px;width:88px">Read More</span>
  <span class="btn btn--ghost" style="left:248px;top:362px;width:88px">Contact Us</span>
  <svg class="arrow" style="left:64px" width="16" height="32" viewBox="0 0 16 32"><polyline points="14,2 2,16 14,30" fill="none" stroke="rgba(255,255,255,.6)" stroke-width="2"/></svg>
  <svg class="arrow" style="left:1120px" width="16" height="32" viewBox="0 0 16 32"><polyline points="2,2 14,16 2,30" fill="none" stroke="rgba(255,255,255,.6)" stroke-width="2"/></svg>
</header>

<!-- ABOUT -->
<section class="about">
  <h2 class="section-title" style="top:643px">About Corventa <span class="blue">Dx</span></h2>
  <div class="rule" style="left:498px;top:703px;width:201px"></div>
  <p class="para" style="left:218px;top:722px;width:764px;text-align:center;font-size:11.5px;line-height:27px">Lorem Ipsum is simply dummy text of the printing and typesetting industry. Lorem Ipsum has been the industry's standard dummy text ever since the 1500s, when an unknown printer took a galley of type and scrambled it to make a type specimen book. It has survived not only five centuries, but also the leap into electronic typesetting, remaining essentially unchanged. It was popularised in the 1960s with the release of Letraset sheets containing Lorem Ipsum passages, and more recently with desktop publishing software like Aldus PageMaker including versions of Lorem Ipsum.</p>
  <span class="btn" style="left:542px;top:893px;width:116px">Read More</span>
  <svg class="wedge" style="left:0;top:932px" width="640" height="74" viewBox="0 0 640 74"><polygon points="0,0 640,72 0,72" fill="var(--blue)"/></svg>
</section>

<!-- SERVICES -->
<section class="services" aria-label="Our Services"></section>
<div class="box-title" style="left:465px;top:1059px;width:103px;height:101px;border-color:#fff;border-right-color:transparent"></div>
<h2 class="abs" style="left:489px;top:1085px;font-size:38px;font-weight:500;color:#fff;white-space:nowrap">Our Services</h2>
<p class="abs" style="left:270px;top:1184px;width:660px;text-align:center;font-size:11.5px;line-height:26px;color:#e6e6e6">Lorem Ipsum is simply dummy text of the printing and typesetting industry. Lorem Ipsum has been the industry's standard dummy text ever since the 1500s.</p>

<article class="card" style="left:143px">
  <div class="card__img" style="background:linear-gradient(135deg,#eef3f7,#b9d3ea 60%,#4f8fd6)" role="img" aria-label="Lab technician in goggles working with test tubes">
    <div class="card__icon"><svg width="34" height="34" viewBox="0 0 34 34"><path d="M6 28C12 22 22 12 28 6M10 30C16 20 20 14 30 10M4 24C14 20 18 14 24 4" fill="none" stroke="#fff" stroke-width="2"/></svg></div>
  </div>
  <h3 class="card__title">Service 1</h3>
  <p class="card__text">Lorem Ipsum is simply dummy text of the printing and typesetting industry.</p>
  <p class="card__link">Read More</p>
</article>
<article class="card" style="left:456px">
  <div class="card__img" style="background:linear-gradient(135deg,#e9f4f6,#a9d7de 55%,#5fb3c2)" role="img" aria-label="Doctor with digital DNA and molecule graphics">
    <div class="card__icon"><svg width="34" height="34" viewBox="0 0 34 34"><path d="M6 28C12 22 22 12 28 6M10 30C16 20 20 14 30 10M4 24C14 20 18 14 24 4" fill="none" stroke="#fff" stroke-width="2"/></svg></div>
  </div>
  <h3 class="card__title">Service 1</h3>
  <p class="card__text">Lorem Ipsum is simply dummy text of the printing and typesetting industry.</p>
  <p class="card__link">Read More</p>
</article>
<article class="card" style="left:769px">
  <div class="card__img" style="background:radial-gradient(ellipse at 50% 50%,#d8e7a8 0%,#3f8fb6 35%,#0c2f55 80%)" role="img" aria-label="Glowing DNA double helix">
    <div class="card__icon"><svg width="34" height="34" viewBox="0 0 34 34"><path d="M6 28C12 22 22 12 28 6M10 30C16 20 20 14 30 10M4 24C14 20 18 14 24 4" fill="none" stroke="#fff" stroke-width="2"/></svg></div>
  </div>
  <h3 class="card__title">Service 1</h3>
  <p class="card__text">Lorem Ipsum is simply dummy text of the printing and typesetting industry.</p>
  <p class="card__link">Read More</p>
</article>

<span class="dot-btn" style="left:560px;top:1706px"></span>
<span class="dot-btn" style="left:605px;top:1706px"><svg width="16" height="10" viewBox="0 0 16 10"><path d="M0 5H14M10 1L14 5L10 9" fill="none" stroke="#333" stroke-width="1.5"/></svg></span>

<!-- FEATURES -->
<svg class="wedge" style="left:0;top:1806px" width="1200" height="78" viewBox="0 0 1200 78"><polygon points="760,0 1200,0 1200,76" fill="var(--blue)"/></svg>

<section class="feature">
  <div class="frame" style="left:157px;top:1904px;width:393px;height:388px"></div>
  <div class="photo" style="left:180px;top:1922px;width:348px;height:349px;background:linear-gradient(135deg,#f1f3f5,#d6dde4 50%,#9bb9d8)" role="img" aria-label="Researcher at a microscope pouring liquid into a beaker"></div>
  <h3 class="feature__title" style="left:608px;top:1972px">Research <span class="blue">Callout</span></h3>
  <div class="rule" style="left:606px;top:2026px;width:128px"></div>
  <p class="para" style="left:606px;top:2052px;width:450px;font-size:11.5px">Lorem Ipsum is simply dummy text of the printing and typesetting industry. Lorem Ipsum has been the industry's standard dummy text ever since the 1500s, when an unknown printer took a galley of type and scrambled it to make a type specimen book. It has survived not only five centuries, but also the leap into electronic typesetting, remaining</p>
  <span class="btn" style="left:603px;top:2205px;width:116px">Read More</span>
</section>

<section class="feature">
  <h3 class="feature__title" style="left:168px;top:2382px">Monitoring or<br>management of <span class="blue">diseases</span></h3>
  <div class="rule" style="left:166px;top:2476px;width:128px"></div>
  <p class="para" style="left:164px;top:2500px;width:450px;font-size:11.5px">Lorem Ipsum is simply dummy text of the printing and typesetting industry. Lorem Ipsum has been the industry's standard dummy text ever since the 1500s, when an unknown printer took a galley of type and scrambled it to make a type specimen book. It has survived not only five centuries, but also the leap into electronic typesetting, remaining essentially unchanged.</p>
  <span class="btn" style="left:162px;top:2647px;width:116px">Read More</span>
  <div class="frame" style="left:643px;top:2336px;width:391px;height:389px"></div>
  <div class="photo" style="left:666px;top:2352px;width:347px;height:352px;background:linear-gradient(135deg,#dfe9f2,#9cc3e6 50%,#3e8fd8)" role="img" aria-label="Technician in protective gear operating laboratory equipment"></div>
</section>

<section class="feature">
  <div class="frame" style="left:157px;top:2748px;width:393px;height:390px"></div>
  <div class="photo" style="left:180px;top:2766px;width:348px;height:350px;background:linear-gradient(135deg,#f4f4f2,#dfe3e6 50%,#8fd0cf)" role="img" aria-label="Scientist working at a bench of sample trays"></div>
  <h3 class="feature__title" style="left:608px;top:2816px">Medical <span class="blue">diagnostics</span></h3>
  <div class="rule" style="left:606px;top:2869px;width:128px"></div>
  <p class="para" style="left:606px;top:2896px;width:450px;font-size:11.5px">Lorem Ipsum is simply dummy text of the printing and typesetting industry. Lorem Ipsum has been the industry's standard dummy text ever since the 1500s, when an unknown printer took a galley of type and scrambled it to make a type specimen book. It has survived not only five centuries, but also the leap into electronic typesetting, remaining</p>
  <span class="btn" style="left:603px;top:3049px;width:116px">Read More</span>
</section>

<!-- TESTIMONIAL -->
<section class="testimonial" role="img" aria-label="Blue backdrop of molecular strands"></section>
<div class="avatar" role="img" aria-label="Client portrait"></div>
<h3 class="abs" style="left:0;width:1200px;top:3394px;text-align:center;font-size:30px;font-weight:600;color:#fff">Daniel Reyes</h3>
<p class="abs" style="left:0;width:1200px;top:3446px;text-align:center;font-size:12px;color:#dbe9ff">Client</p>
<p class="abs" style="left:300px;width:600px;top:3490px;text-align:center;font-size:11.5px;line-height:25px;color:#fff">Lorem Ipsum is simply dummy text of the printing and typesetting industry. Lorem Ipsum has been the industry's standard dummy text ever since the 1500s.</p>
<div class="dots"><i></i><i class="on"></i><i></i></div>

<!-- BLOG -->
<div class="box-title" style="left:507px;top:3683px;width:104px;height:101px;border-color:var(--ink);border-right-color:transparent"></div>
<h2 class="abs" style="left:531px;top:3712px;font-size:38px;font-weight:500;color:var(--ink);white-space:nowrap">Our Blog</h2>

<article>
  <div class="photo" style="left:143px;top:3835px;width:367px;height:239px;background:linear-gradient(135deg,#e9efe9,#b5cfb0 50%,#5f8f5e)" role="img" aria-label="Two researchers examining plants in a greenhouse"></div>
  <div class="meta" style="left:168px;top:4098px">
    <svg width="16" height="16" viewBox="0 0 16 16"><rect x="1" y="3" width="14" height="12" fill="none" stroke="#333" stroke-width="1.5"/><line x1="1" y1="7" x2="15" y2="7" stroke="#333" stroke-width="1.5"/></svg>
    <span>June 13.2019 |</span>
    <svg width="16" height="14" viewBox="0 0 16 14"><path d="M1 1H15V10H6L2 13V10H1Z" fill="#333"/></svg>
    <span>No Comment</span>
  </div>
  <h3 class="post-title" style="left:166px;top:4136px">Lorem Ipsum is a simple</h3>
  <p class="para" style="left:166px;top:4176px;width:330px;font-size:11px;line-height:25px">Lorem Ipsum is simply dummy text of the printing and typesetting industry. Lorem Ipsum has been the industry's standard dummy text</p>
  <span class="more" style="left:166px;top:4266px">Read More</span>
</article>

<article>
  <div class="photo" style="left:549px;top:3835px;width:139px;height:131px;background:linear-gradient(135deg,#5b7d3f,#a8b989 50%,#d7c5b8)" role="img" aria-label="Researcher holding a plant sample"></div>
  <div class="meta" style="left:704px;top:3857px">
    <svg width="16" height="16" viewBox="0 0 16 16"><rect x="1" y="3" width="14" height="12" fill="none" stroke="#333" stroke-width="1.5"/><line x1="1" y1="7" x2="15" y2="7" stroke="#333" stroke-width="1.5"/></svg>
    <span>June 13.2019 |</span>
    <svg width="16" height="14" viewBox="0 0 16 14"><path d="M1 1H15V10H6L2 13V10H1Z" fill="#333"/></svg>
    <span>No Comment</span>
  </div>
  <h3 class="post-title" style="left:702px;top:3884px">Lorem Ipsum is a simple</h3>
  <span class="more" style="left:702px;top:3931px">Read More</span>
</article>
<div class="divider" style="top:3994px"></div>

<article>
  <div class="photo" style="left:549px;top:4025px;width:139px;height:133px;background:linear-gradient(135deg,#dbe7f0,#8fbbe0 55%,#3f7fc0)" role="img" aria-label="Two technicians in masks working with samples"></div>
  <div class="meta" style="left:704px;top:4048px">
    <svg width="16" height="16" viewBox="0 0 16 16"><rect x="1" y="3" width="14" height="12" fill="none" stroke="#333" stroke-width="1.5"/><line x1="1" y1="7" x2="15" y2="7" stroke="#333" stroke-width="1.5"/></svg>
    <span>June 13.2019 |</span>
    <svg width="16" height="14" viewBox="0 0 16 14"><path d="M1 1H15V10H6L2 13V10H1Z" fill="#333"/></svg>
    <span>No Comment</span>
  </div>
  <h3 class="post-title" style="left:702px;top:4075px">Lorem Ipsum is a simple</h3>
  <span class="more" style="left:702px;top:4121px">Read More</span>
</article>
<div class="divider" style="top:4184px"></div>

<article>
  <div class="photo" style="left:549px;top:4212px;width:139px;height:133px;background:linear-gradient(135deg,#e4edf3,#9fc4e2 55%,#4a86c6)" role="img" aria-label="Scientist in a mask examining a test tube"></div>
  <div class="meta" style="left:704px;top:4235px">
    <svg width="16" height="16" viewBox="0 0 16 16"><rect x="1" y="3" width="14" height="12" fill="none" stroke="#333" stroke-width="1.5"/><line x1="1" y1="7" x2="15" y2="7" stroke="#333" stroke-width="1.5"/></svg>
    <span>June 13.2019 |</span>
    <svg width="16" height="14" viewBox="0 0 16 14"><path d="M1 1H15V10H6L2 13V10H1Z" fill="#333"/></svg>
    <span>No Comment</span>
  </div>
  <h3 class="post-title" style="left:702px;top:4263px">Lorem Ipsum is a simple</h3>
  <span class="more" style="left:702px;top:4310px">Read More</span>
</article>

<!-- FOOTER -->
<footer class="footer">
  <div class="footer__links">
    <span style="left:203px">Home</span>
    <span style="left:267px">About Us</span>
    <span style="left:351px">Services</span>
    <span style="left:430px">Blog</span>
    <span style="left:484px">Contact Us</span>
  </div>
  <p class="footer__copy">Copyright © 2019 Corventa Dx.com All right reserved</p>
  <span class="social" style="left:734px"></span>
  <span class="social" style="left:774px"></span>
  <span class="social" style="left:816px"></span>
  <span class="social" style="left:861px"></span>
</footer>

</body>
</html>
```